Postcard - Promoting Maple Ridge Brokers for Farm Clients

We need to develop a postcard (4" X 6") to send out to Agricultural clients.

The content on the email will be:

We understand that farming has variety of risk exposures that can affect your farm and your family’s future.
Maple Ridge Brokers can help you identify and manage those risks by building an insurance program that works for you, your family and your operation. We ensure we understand your risk, you understand your coverage and we sort through the “fine” print together before a loss happens.
Contact Maple Ridge Brokers to arrange a review and meet our team. 1-800-555-0147 fieldcrew@lindenvale.ca

Target Market(s)

We would like 2 separate postcards - one for crop farmers and one for cattle farmers

Industry/Entity Type

Agriculture

Requirements
Must have
• Be remarkable - something that catches your eye, and must have our logo

Please note that this can be 2 sided - potential to have the photo/color side to be the picture and some wording to catch the attention of the individual receiving .... and the back side to be the additional content, which is in the project description.

```html
<!DOCTYPE html>
<html lang="en">
<head>
<meta charset="utf-8">
<title>Maple Ridge Brokers – Crop Farmer Postcard</title>
<link href="https://fonts.googleapis.com/css2?family=EB+Garamond:wght@400;700;800&family=Montserrat:wght@700&display=swap" rel="stylesheet">
<style>
  :root {
    --navy: #141f6b;
    --royal: #1f44b8;
    --card: #f4f4f4;
    --ink: #1b1b1b;
    --rule: #c9c9c9;
    --backdrop: #e6e6e4;
    --wheat-light: #f2c46a;
    --wheat-deep: #b9842f;
  }
  * { box-sizing: border-box; margin: 0; padding: 0; }
  html, body { width: 1200px; height: 900px; overflow: hidden; }
  body { background: var(--backdrop); position: relative; font-family: "EB Garamond", serif; }

  .postcard {
    position: absolute;
    width: 552px;
    height: 367px;
    background: var(--card);
    box-shadow: 0 2px 6px rgba(0,0,0,0.18);
    overflow: hidden;
  }
  .postcard--front { left: 260px; top: 70px; }
  .postcard--back { left: 413px; top: 462px; }

  /* Front */
  .front-art { position: absolute; inset: 0; width: 552px; height: 322px; }
  .brand-block {
    position: absolute; left: 24px; top: 34px; width: 230px;
    text-align: center;
  }
  .brand-mark {
    display: block; width: 22px; height: 22px; margin: 0 auto 10px;
    background: var(--navy);
  }
  .brand-name {
    font-family: "EB Garamond", serif; font-weight: 800;
    color: var(--navy); font-size: 29px; line-height: 1.05; letter-spacing: 0.5px;
    text-transform: uppercase;
  }
  .tagline {
    position: absolute; left: 24px; top: 180px;
    font-size: 19.5px; line-height: 23px; color: var(--navy);
    font-weight: 400;
  }
  .phone-button {
    position: absolute; left: 24px; top: 258px;
    width: 200px; height: 36px;
    background: var(--royal); border-radius: 2px;
    color: #fff; font-weight: 700; font-size: 26px;
    display: flex; align-items: center; justify-content: center;
    letter-spacing: 0.3px;
  }
  .front-banner {
    position: absolute; left: 0; bottom: 0; width: 100%; height: 45px;
    background: var(--navy); color: #fff;
    font-family: "Montserrat", sans-serif; font-weight: 700;
    font-size: 10.6px; line-height: 16px; text-align: center;
    display: flex; flex-direction: column; justify-content: center;
  }

  /* Back */
  .message {
    position: absolute; left: 9px; top: 20px; width: 234px;
    font-size: 7.6px; line-height: 10.8px; color: var(--ink); text-align: justify;
  }
  .message p + p { margin-top: 6px; }
  .stamp-box {
    position: absolute; left: 442px; top: 27px; width: 74px; height: 74px;
    border: 1px solid var(--rule);
  }
  .back-brand {
    position: absolute; left: 40px; top: 160px; width: 180px;
    text-align: center;
  }
  .back-brand .brand-mark { width: 34px; height: 34px; margin-bottom: 12px; }
  .back-brand .brand-name { font-size: 34px; }
  .address-label {
    position: absolute; left: 271px; top: 132px;
    font-family: "Montserrat", sans-serif; font-size: 11px; color: var(--ink); font-weight: 700;
  }
  .address-line {
    position: absolute; left: 285px; width: 230px; height: 1px; background: var(--rule);
  }
  .web-bar {
    position: absolute; left: 0; bottom: 0; width: 250px; height: 39px;
    background: var(--navy); color: #fff;
    font-family: "Montserrat", sans-serif; font-weight: 700; font-size: 11.4px;
    display: flex; align-items: center; justify-content: center; letter-spacing: 0.2px;
  }
</style>
</head>
<body>

<section class="postcard postcard--front">
  <svg class="front-art" viewBox="0 0 552 322" aria-hidden="false">
    <defs>
      <linearGradient id="wheatField" x1="1" y1="0" x2="0" y2="1">
        <stop offset="0" stop-color="var(--wheat-light)"/>
        <stop offset="1" stop-color="var(--wheat-deep)"/>
      </linearGradient>
    </defs>
    <polygon points="406,0 418,0 252,322 240,322" fill="var(--navy)"/>
    <polygon points="418,0 552,0 552,322 252,322" fill="url(#wheatField)"
             role="img" aria-label="Photo of a hand brushing through a golden wheat field at sunset"/>
  </svg>

  <div class="brand-block">
    <span class="brand-mark"></span>
    <div class="brand-name">Maple Ridge<br>Brokers</div>
  </div>

  <p class="tagline">There’s no time like the present.<br>Get a Quote today or call now</p>

  <div class="phone-button">1-800-555-0147</div>

  <div class="front-banner">
    <span>INSURANCE FOR CROP FARMERS TO ENSURE YOUR BUSINESS GROWS &amp; FLOURISHES.</span>
    <span>LET US HELP PROTECT YOUR LIVELIHOOD.</span>
  </div>
</section>

<section class="postcard postcard--back">
  <div class="message">
    <p>We understand that farming has variety of risk exposures that can affect your farm and your family’s future.</p>
    <p>Maple Ridge Brokers can help you identify and manage those risks by building an insurance program that works for you, your family and your operation. We ensure we understand your risk, you understand your coverage and we sort through the “fine” print together before a loss happens.</p>
  </div>

  <div class="stamp-box"></div>

  <div class="back-brand">
    <span class="brand-mark"></span>
    <div class="brand-name">Maple Ridge<br>Brokers</div>
  </div>

  <span class="address-label">To</span>
  <span class="address-line" style="top:191px"></span>
  <span class="address-line" style="top:227px"></span>
  <span class="address-line" style="top:261px"></span>
  <span class="address-line" style="top:298px"></span>

  <div class="web-bar">WWW.FIELDCREW@LINDENVALE.CA</div>
</section>

</body>
</html>
```